GRAPHIC DESIGN FOR RESTAURANT MENU FOR HEALTHY RESTAURANT

I am looking for a graphic design for our menu displayed on a TV screen. Please ensure the file will fit on a TV screen nicely. We are looking for a clean design , with the following items. We would also like to include a couple of photos.
Breakfast:
Protein Chocolate Chip Pancakes - $12.95
Sunny Trail Burrito- $11.95
Tall Barn Omelette - $12.95
Lunch
Butter Chicken - $13.95
Chicken Quesadilla - $13.45
Coconut Garlic Shrimp - $15.95
Goat Cheese Stuffed Chicken - $14.95
Chipotle Steak Wrap - $12.95
Turkey Meatball Fettuccini - $13.45
Chicken Alfredo - $13.45
Chicken Parmesan - $13.95
Pesto Chicken Pasta - $13.45
Steak Bite and Green Stir Fry - $13.45
Asian Chicken Teriyaki - $13.45
Please include our logo
Restaurant

```html
<!DOCTYPE html>
<html lang="en">
<head>
<meta charset="utf-8">
<title>Brightfork Breakfast Menu</title>
<link rel="stylesheet" href="https://fonts.googleapis.com/css2?family=Anton&family=Poppins:wght@700;800&display=swap">
<style>
  :root {
    --green: #8cc021;
    --grey: #9a9a9a;
    --cream: #fcf8f1;
    --white: #ffffff;
    --photo-warm-1: #b98a6e;
    --photo-warm-2: #efe4d6;
    --plate-1: #f3c24a;
    --plate-2: #e9e6e2;
  }
  * { margin: 0; padding: 0; box-sizing: border-box; }
  html, body { width: 1200px; height: 675px; overflow: hidden; background: var(--white); }
  .menu-board {
    position: relative;
    width: 1200px;
    height: 675px;
    overflow: hidden;
    background: var(--white);
    font-family: "Poppins", sans-serif;
  }
  .top-band {
    position: absolute;
    left: 0; top: 0;
    width: 1200px; height: 265px;
    background: var(--cream);
  }
  .hero-photo {
    position: absolute;
    left: 0; top: 0;
    width: 592px; height: 265px;
    background: linear-gradient(90deg, var(--photo-warm-1) 0%, #d7bba3 60%, var(--photo-warm-2) 100%);
  }
  .dish-photo {
    position: absolute;
    left: 629px; top: 156px;
    width: 508px; height: 242px;
    border-radius: 26px;
    background: radial-gradient(ellipse at 50% 55%, var(--plate-1) 0%, #e9c780 45%, var(--plate-2) 75%, rgba(233,230,226,0) 100%);
  }
  .brand {
    position: absolute;
    right: 63px; top: 33px;
    text-align: right;
  }
  .brand-name {
    font-family: "Poppins", sans-serif;
    font-weight: 800;
    font-size: 62px;
    line-height: 64px;
    letter-spacing: 1px;
    color: var(--grey);
  }
  .brand-tagline {
    margin-top: 2px;
    font-weight: 700;
    font-size: 20px;
    line-height: 24px;
    color: var(--green);
    letter-spacing: -0.2px;
  }
  .brand-tagline .divider { display: inline-block; margin: 0 8px; }
  .section-title {
    position: absolute;
    left: 62px; top: 278px;
    font-family: "Anton", sans-serif;
    font-size: 124px;
    line-height: 130px;
    letter-spacing: 4px;
    color: var(--green);
  }
  .menu-items { list-style: none; }
  .menu-item {
    position: absolute;
    left: 64px;
    width: 990px;
    display: flex;
    justify-content: space-between;
    align-items: flex-start;
  }
  .item-name {
    font-weight: 800;
    font-size: 38px;
    line-height: 49px;
    letter-spacing: 1.5px;
    color: var(--grey);
  }
  .item-price {
    width: 134px;
    font-weight: 800;
    font-size: 38px;
    line-height: 49px;
    letter-spacing: 1.5px;
    color: var(--green);
  }
  .item-pancakes { top: 421px; }
  .item-burrito { top: 534px; }
  .item-omelette { top: 598px; }
</style>
</head>
<body>
  <main class="menu-board">
    <div class="top-band"></div>
    <div class="hero-photo" role="img" aria-label="Photo of a smiling couple sharing a forkful of breakfast at a cafe table"></div>
    <div class="dish-photo" role="img" aria-label="Photo of a vegetable omelette with wholegrain toast on a white square plate"></div>

    <header class="brand">
      <div class="brand-name">BRIGHTFORK</div>
      <div class="brand-tagline">HEALTHY KITCHEN<span class="divider">|</span>MEAL PREP</div>
    </header>

    <h1 class="section-title">Breakfast</h1>

    <ul class="menu-items">
      <li class="menu-item item-pancakes">
        <span class="item-name">Protein Chocolate<br>Chip Pancakes</span>
        <span class="item-price">$12.95</span>
      </li>
      <li class="menu-item item-burrito">
        <span class="item-name">Sunny Trail Burrito</span>
        <span class="item-price">$11.95</span>
      </li>
      <li class="menu-item item-omelette">
        <span class="item-name">Tall Barn Omelette</span>
        <span class="item-price">$12.95</span>
      </li>
    </ul>
  </main>
</body>
</html>
```